Quorvex - Automated robotic Inspection with AI need new business cards

We need a new design of our business cards. The company is focused on automated quality control at high speed with unmatched results. We have a logo but need a more forward leaning business card that shows that we are delivering cutting edge technology.

Contact Information for Business Card

Name
Position
Adress
Phone
Email
e.g.
Lena Holmqvist
Chief Financial Officer (CFO)

Quorvex Sweden AB
Bruksvägen 14, SE-175 43 JÄRFÄLLA, Sweden
Mobile: +46735 21 47 83 | Office: +46 8 61 94 27
www.quorvex-example.com

Font styles to use
Sans Serif

```html
<!DOCTYPE html>
<html lang="en">
<head>
<meta charset="utf-8">
<title>Quorvex Business Card</title>
<link rel="stylesheet" href="https://fonts.googleapis.com/css2?family=Lato:wght@400;700;900&display=swap">
<style>
  :root {
    --backdrop: #d2d2ce;
    --card-white: #ffffff;
    --brand-blue: #1d5a8a;
    --brand-blue-soft: #2a6797;
    --ink-grey: #555a60;
    --divider: #1d5a8a;
  }
  * { box-sizing: border-box; margin: 0; padding: 0; }
  html, body { width: 1200px; height: 801px; overflow: hidden; }
  body {
    background: var(--backdrop);
    font-family: "Lato", sans-serif;
    position: relative;
  }
  .card {
    position: absolute;
    top: 250px;
    width: 520px;
    height: 300px;
    box-shadow: 0 10px 24px rgba(0,0,0,0.22);
  }
  .card-front { left: 50px; background: var(--card-white); }
  .card-back { left: 630px; background: var(--brand-blue); overflow: hidden; }

  .brand-name {
    font-family: "Lato", sans-serif;
    font-weight: 900;
    letter-spacing: 1px;
    display: flex;
    align-items: center;
    gap: 12px;
  }
  .brand-dot { width: 18px; height: 18px; border-radius: 50%; }

  .card-front .brand-name {
    position: absolute; left: 40px; top: 138px;
    font-size: 36px; color: var(--brand-blue);
  }
  .card-front .brand-dot { background: var(--brand-blue); }

  .front-divider {
    position: absolute; left: 258px; top: 60px;
    width: 1.5px; height: 180px; background: var(--divider);
  }
  .contact-block {
    position: absolute; left: 282px; top: 40px; right: 18px;
    color: var(--ink-grey);
  }
  .person-name { font-size: 21px; font-weight: 900; color: var(--brand-blue); line-height: 1.1; }
  .person-role { font-size: 11.5px; margin-top: 3px; }
  .company-address { font-size: 10.5px; line-height: 1.4; margin-top: 16px; }
  .contact-list { list-style: none; margin-top: 16px; font-size: 10.5px; line-height: 1.55; }
  .contact-list li { display: flex; align-items: center; gap: 8px; }
  .contact-list svg { width: 11px; height: 11px; flex: none; fill: var(--brand-blue); }

  .back-pattern {
    position: absolute; inset: 0;
    background: linear-gradient(135deg, var(--brand-blue-soft), var(--brand-blue) 60%);
  }
  .card-back .brand-name {
    position: absolute; right: 42px; bottom: 70px;
    font-size: 40px; color: var(--card-white);
  }
  .card-back .brand-dot { background: var(--card-white); }
</style>
</head>
<body>
  <section class="card card-front" aria-label="Business card front">
    <div class="brand-name"><span class="brand-dot"></span>QUORVEX</div>
    <div class="front-divider"></div>
    <div class="contact-block">
      <div class="person-name">Lena Holmqvist</div>
      <div class="person-role">Chief Financial Officer</div>
      <div class="company-address">
        Quorvex Sweden AB<br>
        Bruksvägen 14, SE-175 43 JÄRFÄLLA,<br>
        Sweden
      </div>
      <ul class="contact-list">
        <li><svg viewBox="0 0 12 12"><path d="M2 1h2.5l1 3-1.5 1a6 6 0 0 0 3 3l1-1.5 3 1V10a1 1 0 0 1-1 1A9 9 0 0 1 1 2a1 1 0 0 1 1-1z"/></svg>+46 8 61 94 27</li>
        <li><svg viewBox="0 0 12 12"><path d="M3 0h6a1 1 0 0 1 1 1v10a1 1 0 0 1-1 1H3a1 1 0 0 1-1-1V1a1 1 0 0 1 1-1zm0 1.5v8h6v-8z"/></svg>+46735 21 47 83</li>
        <li><svg viewBox="0 0 12 12"><path d="M0 2h12v8H0zm1 1v.3l5 3.2 5-3.2V3z"/></svg>info@quorvex-example.com</li>
        <li><svg viewBox="0 0 12 12"><path d="M6 0a6 6 0 1 0 0 12A6 6 0 0 0 6 0zm0 1.2a4.8 4.8 0 0 1 0 9.6 4.8 4.8 0 0 1 0-9.6zM1.5 5.4h9v1.2h-9zM5.4 1.5h1.2v9H5.4z"/></svg>www.quorvex-example.com</li>
      </ul>
    </div>
  </section>

  <section class="card card-back" aria-label="Business card back">
    <div class="back-pattern" role="img" aria-label="Faint repeating brand pattern in deep blue tones"></div>
    <div class="brand-name"><span class="brand-dot"></span>QUORVEX</div>
  </section>
</body>
</html>
```